Tranquil Pathway Business Card

Logo attached. (will be printing onto thick white/off white textured card)

Double sided business card for two Therapists working at Tranquil Pathway.

Require one design, but with different name and mobile numbers on each card.

Target Market(s)

Medical, Health

Industry/Entity Type

Business

Contact Information for Business Card

Need one business card design, but a separate card for each person - Colin Marchetti and Marieke de Boeckx.

FRONT OF CARD

Logo

Name (Colin Marchetti on one card, Marieke de Boeckx on the other)
Professional Clinical Hypnotherapist

Consulting Rooms (Near Lindqvist Hospital)
482 Brackenfield Road
Dunmore VIC 3987

Colin@TranquilPathway.example.au OR Marieke@TranquilPathway.example.au

Mobile: 0455 872 604 (for Colin) OR
Mobile: 0467 290 518 (for Marieke)

BACK OF CARD

Logo

Website: www.TranquilPathway.example.au

Phone: 1300 958 471

Requirements
Must have
• Text and logo only. No additiional graphics.

```html
<!DOCTYPE html>
<html lang="en">
<head>
<meta charset="utf-8">
<title>Tranquil Pathway – Business Card</title>
<link rel="stylesheet" href="https://fonts.googleapis.com/css2?family=Arimo:wght@700&family=Source+Sans+3:ital,wght@0,400;0,600;1,400&display=swap">
<style>
  :root {
    --navy: #232b5e;
    --paper: #eeefee;
    --grey: #5f5f5f;
    --ring-grey: #626262;
    --subtitle: #c3c5d2;
    --faint: rgba(255,255,255,0.07);
  }
  * { margin: 0; padding: 0; box-sizing: border-box; }
  html, body { width: 1200px; height: 731px; overflow: hidden; background: var(--paper); }
  .card { position: relative; width: 1200px; height: 731px; display: flex; }
  .card-front {
    position: relative; width: 638px; height: 731px; background: var(--navy); overflow: hidden;
  }
  .card-back { position: relative; flex: 1; height: 731px; background: var(--paper); }

  .faint-mark { position: absolute; left: 137px; top: 326px; }

  .holder { position: absolute; left: 0; width: 746px; top: 302px; text-align: center; }
  .holder-name {
    font-family: "Arimo", Arial, sans-serif; font-weight: 700; font-size: 49px;
    color: #fff; line-height: 1; letter-spacing: 0.2px;
  }
  .holder-title {
    margin-top: 12px; font-family: "Source Sans 3", sans-serif; font-size: 20px;
    color: var(--subtitle); line-height: 1;
  }

  .brand { position: absolute; left: 662px; top: 117px; display: flex; align-items: center; gap: 24px; }
  .brand-dot { width: 132px; height: 132px; border-radius: 50%; background: var(--navy); }
  .brand-name {
    font-family: "Arimo", Arial, sans-serif; font-weight: 700; font-size: 38px;
    line-height: 1.05; color: var(--navy); letter-spacing: 1px; text-transform: uppercase;
  }

  .contacts {
    position: absolute; left: 654px; top: 438px; list-style: none;
    font-family: "Source Sans 3", sans-serif; font-size: 18px; color: var(--grey);
  }
  .contact-row { display: flex; align-items: flex-start; margin-bottom: 7px; }
  .contact-icon {
    width: 43px; height: 43px; border-radius: 50%; background: var(--ring-grey);
    display: flex; align-items: center; justify-content: center; flex-shrink: 0;
  }
  .contact-label { width: 70px; margin-left: 7px; line-height: 43px; }
  .contact-value { line-height: 43px; }
  .address { padding-top: 10px; line-height: 1.2; }
  .address-venue { font-weight: 600; display: block; }
  .address-note { font-style: italic; font-size: 12.5px; display: block; margin: 1px 0 2px; }
</style>
</head>
<body>
<main class="card">
  <section class="card-front">
    <svg class="faint-mark" width="276" height="276" viewBox="0 0 276 276" aria-hidden="true">
      <circle cx="138" cy="138" r="132" fill="none" stroke="var(--faint)" stroke-width="12"/>
    </svg>
    <div class="holder">
      <h1 class="holder-name">Colin Marchetti</h1>
      <p class="holder-title">Professional Clinical Hypnotherapist</p>
    </div>
  </section>

  <section class="card-back">
    <div class="brand" style="left:24px">
      <div class="brand-dot"></div>
      <div class="brand-name">Tranquil<br>Pathway</div>
    </div>

    <ul class="contacts" style="left:16px">
      <li class="contact-row">
        <span class="contact-icon">
          <svg width="16" height="24" viewBox="0 0 16 24" aria-hidden="true">
            <rect x="2" y="1" width="12" height="22" rx="2.5" fill="none" stroke="#fff" stroke-width="1.8"/>
            <rect x="4.5" y="4" width="7" height="13" fill="#fff"/>
          </svg>
        </span>
        <span class="contact-label">Mobile:</span>
        <span class="contact-value">0455 872 604</span>
      </li>
      <li class="contact-row">
        <span class="contact-icon">
          <svg width="22" height="16" viewBox="0 0 22 16" aria-hidden="true">
            <rect x="1" y="1" width="20" height="14" fill="#fff"/>
            <polyline points="1,1 11,9 21,1" fill="none" stroke="var(--ring-grey)" stroke-width="1.4"/>
          </svg>
        </span>
        <span class="contact-label">Email:</span>
        <span class="contact-value">Colin@TranquilPathway.example.au</span>
      </li>
      <li class="contact-row">
        <span class="contact-icon">
          <svg width="16" height="22" viewBox="0 0 16 22" aria-hidden="true">
            <path d="M8 1a7 7 0 0 1 7 7c0 5-7 13-7 13S1 13 1 8a7 7 0 0 1 7-7z" fill="#fff"/>
            <circle cx="8" cy="8" r="2.6" fill="var(--ring-grey)"/>
          </svg>
        </span>
        <span class="contact-label">Address:</span>
        <span class="address">
          <span class="address-venue">Consulting Rooms</span>
          <span class="address-note">(Near Lindqvist Hospital)</span>
          482 Brackenfield Road, Dunmore VIC 3987
        </span>
      </li>
    </ul>
  </section>
</main>
</body>
</html>
```